Advertisement Design

I'm looking for a post card sized advertisement piece that I will be dropping off to commercial and residential customers.
On one side I want it promoting carpet cleaning services and on the other side dryer vent cleaning services.
I've uploaded two different layouts of my company logo for you to choice from.
One batch will be printed with my Michigan Number
One batch will be printed with my Tennessee number
Will share contact numbers with the winner so just use a make up number
555-318-4729

```html
<!DOCTYPE html>
<html lang="en">
<head>
<meta charset="utf-8">
<title>Carpet Cleaning Postcard</title>
<link rel="stylesheet" href="https://fonts.googleapis.com/css2?family=Montserrat:wght@400;500;700&family=Oswald:wght@600&display=swap">
<style>
  :root {
    --page-bg: #e9e9e9;
    --card-bg: #ffffff;
    --blue-light: #1a7fc1;
    --blue-mid: #0a77bd;
    --blue-dark: #0b4f98;
    --blue-deep: #063f8a;
    --pill-grey: #9b9b9b;
    --text-white: #ffffff;
    --logo-grey: #4a4a4a;
  }
  * { box-sizing: border-box; margin: 0; padding: 0; }
  html, body { width: 1200px; height: 1200px; overflow: hidden; background: var(--page-bg); }
  .postcard {
    position: absolute; left: 50px; top: 200px;
    width: 1100px; height: 800px;
    background: var(--card-bg);
    overflow: hidden;
    font-family: "Montserrat", sans-serif;
  }
  .postcard__bands { position: absolute; inset: 0; }
  .postcard__photo {
    position: absolute; left: 0; top: 0; width: 571px; height: 657px;
    background: linear-gradient(160deg, #d9dcdf 0%, #c3c7cb 35%, #8e9398 60%, #e4e3e0 100%);
  }
  .headline {
    position: absolute; left: 612px; top: 46px;
    font-size: 56px; line-height: 60px; letter-spacing: 0.5px;
  }
  .headline__light { display: block; font-weight: 500; color: var(--blue-light); }
  .headline__bold { display: block; font-weight: 700; color: var(--blue-dark); }
  .services { position: absolute; left: 614px; top: 322px; list-style: none; }
  .services__item {
    display: block; width: max-content;
    height: 41px; line-height: 41px;
    padding: 0 16px 0 14px; margin-bottom: 13px;
    border-radius: 7px;
    color: var(--text-white); font-size: 23px; font-weight: 500;
  }
  .services__item::before { content: "• "; }
  .services__item--blue { background: var(--blue-dark); }
  .services__item--grey { background: var(--pill-grey); }
  .contact {
    position: absolute; left: 636px; top: 580px;
    display: flex; align-items: center; gap: 22px;
    color: var(--text-white);
  }
  .contact__icon { width: 48px; height: 30px; }
  .contact__number {
    font-family: "Oswald", sans-serif; font-weight: 600;
    font-size: 66px; line-height: 78px; letter-spacing: 0.5px;
  }
  .brand {
    position: absolute; left: 722px; top: 712px;
    display: flex; align-items: center; gap: 14px;
  }
  .brand__square { width: 40px; height: 40px; background: var(--blue-mid); }
  .brand__name {
    font-size: 22px; font-weight: 500; color: var(--blue-dark);
    letter-spacing: 0.5px; line-height: 1.1;
  }
</style>
</head>
<body>
  <div class="postcard">
    <div class="postcard__photo" role="img" aria-label="Photo of a person vacuuming a light carpet in a bright living room"></div>

    <svg class="postcard__bands" viewBox="0 0 1100 800" width="1100" height="800" aria-hidden="true">
      <defs>
        <linearGradient id="bandTop" x1="0" x2="1" y1="0" y2="0">
          <stop offset="0" stop-color="#063f8a"/>
          <stop offset="1" stop-color="#0a7fc0"/>
        </linearGradient>
        <linearGradient id="bandBottom" x1="0" x2="1" y1="0" y2="0">
          <stop offset="0" stop-color="#0a80c2"/>
          <stop offset="1" stop-color="#063f8a"/>
        </linearGradient>
      </defs>
      <path d="M620 559 H1100 V681 H0 V657 H486 Q506 657 520 636 L570 580 Q588 559 620 559 Z" fill="url(#bandTop)"/>
      <rect x="0" y="657" width="1100" height="24" fill="#06469a"/>
      <path d="M0 681 H790 Q750 681 735 715 L705 775 Q692 800 660 800 H0 Z" fill="url(#bandBottom)"/>
    </svg>

    <h1 class="headline">
      <span class="headline__light">Professional</span>
      <span class="headline__light">Carpet</span>
      <span class="headline__bold">Cleaning</span>
      <span class="headline__bold">Services</span>
    </h1>

    <ul class="services">
      <li class="services__item services__item--blue">Domestic Cleaning</li>
      <li class="services__item services__item--grey">Office Cleaning</li>
      <li class="services__item services__item--blue">End Of Tenancy Cleaning</li>
      <li class="services__item services__item--grey">Regular Cleaning</li>
    </ul>

    <div class="contact">
      <svg class="contact__icon" viewBox="0 0 48 30" aria-hidden="true">
        <path d="M2 10 Q24 -4 46 10 L44 15 L35 13 L34 8 Q24 5 14 8 L13 13 L4 15 Z" fill="#fff"/>
        <path d="M14 14 H34 L40 28 H8 Z" fill="#fff"/>
      </svg>
      <span class="contact__number">555-318-4729</span>
    </div>

    <div class="brand">
      <span class="brand__square"></span>
      <span class="brand__name">Loomleaf Property Services</span>
    </div>
  </div>
</body>
</html>
```